Christmas Card 2021

We need a design for a Christmas Card in the format DIN A5 (148 x 210 mm). KELOR is an Austrian company with branches all over Europe. KELOR handles international claims for insurance companies. The Christmas Card will be sent to all our clients all over Europe and beyond.
The design must include our logo (see uploaded file). The color blue that we use is: CMYK: 100/16/0/27 or RGB: 0/114/168.
The card must have this text:
Fröhliche Weihnachten und ein gutes neues Jahr!
Merry Christmas and Happy New Year!
Joyeux Noël et bonne année !
Optional you can use our key visual (see uploaded file).
Optional you can use our motto text: worldwide claims service
We are looking forward to your design!
Kind regards
Lukas

```html
<!DOCTYPE html>
<html lang="en">
<head>
<meta charset="utf-8">
<title>KELOR Christmas Card 2021</title>
<link rel="stylesheet" href="https://fonts.googleapis.com/css2?family=Cinzel:wght@500&family=Quicksand:wght@400;700&display=swap">
<style>
  :root {
    --navy-deep: #1b2544;
    --navy: #27324f;
    --navy-light: #3a4668;
    --branch-blue: #5f6f9c;
    --bauble-glow: #8a9cc8;
    --text-white: #f3f4f8;
  }
  * { margin: 0; padding: 0; box-sizing: border-box; }
  html, body {
    width: 1200px;
    height: 730px;
    overflow: hidden;
    background: var(--navy-deep);
  }
  .card {
    position: relative;
    width: 1200px;
    height: 730px;
    overflow: hidden;
    background: linear-gradient(100deg, var(--navy-deep) 0%, var(--navy) 55%, var(--navy-light) 100%);
  }
  .tree-illustration {
    position: absolute;
    left: 0;
    top: 0;
    width: 730px;
    height: 730px;
    background:
      radial-gradient(circle at 230px 260px, rgba(138,156,200,0.55) 0%, rgba(138,156,200,0) 18%),
      radial-gradient(circle at 440px 170px, rgba(138,156,200,0.45) 0%, rgba(138,156,200,0) 15%),
      radial-gradient(circle at 150px 470px, rgba(138,156,200,0.4) 0%, rgba(138,156,200,0) 15%),
      radial-gradient(circle at 335px 585px, rgba(138,156,200,0.45) 0%, rgba(138,156,200,0) 16%),
      radial-gradient(ellipse at 30% 50%, rgba(95,111,156,0.75) 0%, rgba(95,111,156,0.35) 45%, rgba(39,50,79,0) 75%);
  }
  .greetings {
    position: absolute;
    left: 560px;
    top: 225px;
    width: 620px;
    text-align: center;
    color: var(--text-white);
    font-family: "Quicksand", sans-serif;
    font-weight: 400;
    font-size: 22px;
    line-height: 1;
  }
  .greeting { margin-bottom: 40px; white-space: nowrap; }
  .greeting-caps {
    font-family: "Cinzel", serif;
    font-weight: 500;
    font-size: 20px;
    letter-spacing: -0.3px;
  }
  .brand-name {
    position: absolute;
    left: 768px;
    top: 615px;
    width: 200px;
    text-align: center;
    color: var(--text-white);
    font-family: "Quicksand", sans-serif;
    font-weight: 700;
    font-size: 36px;
    letter-spacing: 1px;
  }
</style>
</head>
<body>
  <main class="card">
    <div class="tree-illustration" role="img" aria-label="Illustration of dark blue fir branches with hanging blue Christmas baubles and soft sparkling lights"></div>

    <section class="greetings">
      <p class="greeting" lang="de"><span class="greeting-caps">FRÖHLICHE WEIHNACHTEN</span> und ein gutes neues Jahr!</p>
      <p class="greeting" lang="en"><span class="greeting-caps">MERRY CHRISTMAS</span> and Happy New Year!</p>
      <p class="greeting" lang="fr"><span class="greeting-caps">JOYEUX NOËL</span> et bonne année!</p>
    </section>

    <p class="brand-name">KELOR</p>
  </main>
</body>
</html>
```